Business card and stationary design-mobile medical imaging
Brantwell Scanning, Inc.
Please check top right message box
I like the shade of purple in #13! Can you try the design in #3 with the purple from 13, and use the little symbols for phone, email, web instead of 'PEW'? I'd like to keep the address with no symbol. Thank you!!
#4-12 I really like the designs. It's sometimes difficult to appreciate colors from a computer screen. Just making sure the color is deep purple. I don't want the color to look blue at all. Thank you for all of your work!!
1-3 could you try even darker purple?

```html
<!DOCTYPE html>
<html lang="en">
<head>
<meta charset="utf-8">
<title>Brantwell Scanning, Inc. — Stationery</title>
<link rel="stylesheet" href="https://fonts.googleapis.com/css2?family=Lato:wght@400;700&display=swap">
<style>
  :root{
    --bg:#1c1c1e;
    --paper:#ffffff;
    --paper-shade:#eeeef0;
    --fold-line:#d6d6da;
    --ink:#4a4a4f;
    --ink-soft:#8a8a90;
    --purple:#4a1658;
    --purple-dark:#2e0b38;
    --grey-dark:#5c5c62;
  }
  *{box-sizing:border-box;margin:0;padding:0}
  html,body{width:1200px;height:710px;overflow:hidden;background:var(--bg);font-family:"Lato",sans-serif;color:var(--ink)}
  .stage{position:relative;width:1200px;height:710px}
  .piece{position:absolute;background:var(--paper);overflow:hidden;box-shadow:0 6px 18px rgba(0,0,0,.5)}
  .swoosh{position:absolute;left:0;bottom:0;width:100%;display:block}
  .wordmark{font-weight:700;color:var(--grey-dark);letter-spacing:.02em;line-height:1.1;display:flex;align-items:center;gap:6px}
  .wordmark .dot{width:9px;height:9px;background:var(--purple);border-radius:50%;flex:none}
  .tagline{font-size:7px;color:var(--purple);letter-spacing:.06em;white-space:nowrap}
  .contact{font-size:7px;line-height:1.6;color:var(--ink-soft);white-space:nowrap}

  /* letterhead */
  .letterhead{left:215px;top:45px;width:440px;height:620px}
  .letterhead .wordmark{position:absolute;left:34px;top:40px;font-size:20px;width:200px}
  .letterhead .tagline{position:absolute;left:49px;top:98px}
  .letterhead .contact{position:absolute;left:260px;top:34px}
  .letterhead .footer-web{position:absolute;left:0;right:0;bottom:10px;text-align:center;font-size:7px;color:#fff;letter-spacing:.05em}

  /* business cards */
  .card{width:178px;height:102px;border-radius:6px}
  .card-front{left:20px;top:210px}
  .card-front .wordmark{position:absolute;left:9px;top:18px;font-size:10px;width:92px;gap:5px}
  .card-front .wordmark .dot{width:7px;height:7px}
  .card-front .tagline{position:absolute;left:9px;top:48px;font-size:5px}
  .card-front .person{position:absolute;left:102px;top:14px;font-size:7px;color:var(--ink);white-space:nowrap}
  .card-front .person span{display:block;color:var(--ink-soft);font-size:5.5px}
  .card-front .contact{position:absolute;left:102px;top:38px;font-size:5.5px;line-height:1.75}
  .icon{display:inline-block;width:6px;height:6px;vertical-align:-1px;margin-right:3px}
  .card-back{left:20px;top:345px;background:linear-gradient(135deg,#a7a7ad,#6e6e74 60%,#505056)}
  .card-back .wordmark{position:absolute;left:0;right:0;top:42px;justify-content:center;color:#fff;font-size:12px;white-space:nowrap}

  /* envelopes */
  .envelope{width:440px;height:180px}
  .envelope .folds{position:absolute;inset:0;width:100%;height:100%}
  .env-purple{left:690px;top:25px}
  .env-grey{left:735px;top:130px}
  .env-white{left:700px;top:245px}
  .env-front{left:690px;top:480px;height:190px}
  .envelope .flap-mark{position:absolute;left:0;right:0;top:20px;justify-content:center;font-size:11px;white-space:nowrap}
  .env-purple .flap-mark,.env-grey .flap-mark{color:#fff}
  .env-white .flap-mark{color:var(--grey-dark)}
  .env-front .wordmark{position:absolute;left:22px;top:24px;font-size:14px;white-space:nowrap}
  .env-front .tagline{position:absolute;left:37px;top:48px;font-size:6px}
  .env-front .contact{position:absolute;left:37px;top:62px;font-size:6px}
</style>
</head>
<body>
<main class="stage">

  <!-- Letterhead -->
  <section class="piece letterhead">
    <div class="wordmark"><i class="dot"></i>Brantwell Scanning, Inc.</div>
    <div class="tagline">Mobile Diagnostic Services</div>
    <div class="contact">410 Harbor Lane<br>Salem, OR 97301<br>555.201.4480<br>info@brantwell.com</div>
    <svg class="swoosh" viewBox="0 0 440 60" height="60" preserveAspectRatio="none" aria-hidden="true">
      <defs><linearGradient id="lhGrey" x1="0" x2="1"><stop offset="0" stop-color="#c9c9ce"/><stop offset="1" stop-color="#6d6d73"/></linearGradient></defs>
      <path d="M0 38 Q220 18 440 14 L440 60 L0 60Z" fill="url(#lhGrey)"/>
      <path d="M0 44 Q220 24 440 20 L440 60 L0 60Z" fill="#6a6a70"/>
      <path d="M0 40 Q220 20 440 16" stroke="var(--purple)" stroke-width="2.5" fill="none"/>
    </svg>
    <div class="footer-web">www.brantwell.com</div>
  </section>

  <!-- Business card front -->
  <section class="piece card card-front">
    <div class="wordmark"><i class="dot"></i>Brantwell Scanning, Inc.</div>
    <div class="tagline">Mobile Diagnostic Services</div>
    <div class="person">Dana Whitfield<span>Operations Director</span></div>
    <div class="contact">
      <div><svg class="icon" viewBox="0 0 10 10"><path d="M2 1h2l1 2.5-1.3 1a5 5 0 0 0 2.8 2.8l1-1.3L10 6v2a1 1 0 0 1-1 1A8 8 0 0 1 1 2a1 1 0 0 1 1-1z" fill="var(--purple)"/></svg>555.201.4480</div>
      <div><svg class="icon" viewBox="0 0 10 10"><rect x="1" y="1" width="8" height="8" rx="1" fill="var(--purple)"/><path d="M3 4h4M3 6h4" stroke="#fff"/></svg>555.201.4481</div>
      <div><svg class="icon" viewBox="0 0 10 10"><rect x=".5" y="2" width="9" height="6" fill="var(--purple)"/><path d="M.5 2l4.5 3.5L9.5 2" stroke="#fff" fill="none"/></svg>dana@brantwell.com</div>
      <div><svg class="icon" viewBox="0 0 10 10"><circle cx="5" cy="5" r="4.2" fill="none" stroke="var(--purple)"/><path d="M1 5h8M5 .8v8.4" stroke="var(--purple)"/></svg>www.brantwell.com</div>
    </div>
    <svg class="swoosh" viewBox="0 0 178 20" height="20" preserveAspectRatio="none" aria-hidden="true">
      <path d="M0 10 Q90 4 178 3 L178 20 L0 20Z" fill="#8a8a90"/>
      <path d="M0 11 Q90 5 178 4" stroke="var(--purple)" stroke-width="1.5" fill="none"/>
    </svg>
  </section>

  <!-- Business card back -->
  <section class="piece card card-back">
    <div class="wordmark">Brantwell Scanning, Inc.</div>
  </section>

  <!-- Envelope back, purple flap -->
  <section class="piece envelope env-purple">
    <svg class="folds" viewBox="0 0 460 196" preserveAspectRatio="none" aria-hidden="true">
      <path d="M0 196 L200 120 Q230 110 260 120 L460 196" fill="var(--paper-shade)" stroke="var(--fold-line)"/>
      <path d="M0 0 H460 V20 L250 118 Q230 126 210 118 L0 20Z" fill="var(--purple)"/>
      <path d="M0 20 L210 118 Q230 126 250 118 L460 20" stroke="var(--purple-dark)" stroke-width="2" fill="none"/>
    </svg>
    <div class="wordmark flap-mark">Brantwell Scanning, Inc.</div>
  </section>

  <!-- Envelope back, grey flap -->
  <section class="piece envelope env-grey">
    <svg class="folds" viewBox="0 0 460 196" preserveAspectRatio="none" aria-hidden="true">
      <defs><linearGradient id="flapGrey" x1="0" x2="1"><stop offset="0" stop-color="#b5b5ba"/><stop offset="1" stop-color="#6a6a70"/></linearGradient></defs>
      <path d="M0 196 L200 120 Q230 110 260 120 L460 196" fill="var(--paper-shade)" stroke="var(--fold-line)"/>
      <path d="M0 0 H460 V20 L250 118 Q230 126 210 118 L0 20Z" fill="url(#flapGrey)"/>
    </svg>
    <div class="wordmark flap-mark">Brantwell Scanning, Inc.</div>
  </section>

  <!-- Envelope back, white flap -->
  <section class="piece envelope env-white">
    <svg class="folds" viewBox="0 0 460 196" preserveAspectRatio="none" aria-hidden="true">
      <path d="M0 196 L200 120 Q230 110 260 120 L460 196" fill="var(--paper-shade)" stroke="var(--fold-line)"/>
      <path d="M0 0 H460 V20 L250 118 Q230 126 210 118 L0 20Z" fill="var(--paper)"/>
      <path d="M0 20 L210 118 Q230 126 250 118 L460 20" stroke="var(--fold-line)" stroke-width="1.5" fill="none"/>
    </svg>
    <div class="wordmark flap-mark">Brantwell Scanning, Inc.</div>
  </section>

  <!-- Envelope front -->
  <section class="piece envelope env-front">
    <div class="wordmark"><i class="dot"></i>Brantwell Scanning, Inc.</div>
    <div class="tagline">Mobile Diagnostic Services</div>
    <div class="contact">410 Harbor Lane<br>Salem, OR 97301</div>
    <svg class="swoosh" viewBox="0 0 460 40" height="40" preserveAspectRatio="none" aria-hidden="true">
      <defs><linearGradient id="envGrey" x1="0" x2="1"><stop offset="0" stop-color="#d0d0d4"/><stop offset="1" stop-color="#6d6d73"/></linearGradient></defs>
      <path d="M0 26 Q230 10 460 6 L460 40 L0 40Z" fill="url(#envGrey)"/>
      <path d="M0 28 Q230 12 460 8" stroke="var(--purple)" stroke-width="2" fill="none"/>
    </svg>
  </section>

</main>
</body>
</html>
```